Football and sports news website

I am looking for a good design and website for a Sports news and Football website. The website will carry mainly football news from different leagues across Europe and the rest of the World. There will be a category for football, tennis, basketball, cricket,ruby. My website should be contemporary and attractive. My favorite colors are blue, purple,orange and red.
Designers can take a clue from http://varnolite.com
There will be column at the under of every news page in which readers of the article can comment.

News

Coded - Design and coding required

```html
<!DOCTYPE html>
<html lang="en">
<head>
<meta charset="utf-8">
<title>Corvan Sports – Football News</title>
<link rel="stylesheet" href="https://fonts.googleapis.com/css2?family=Nunito+Sans:wght@400;600;700;800&family=Open+Sans:ital,wght@0,400;0,600;0,700;1,400&display=swap">
<style>
:root{
  --purple:#3e0b57;
  --purple-light:#5c1c7a;
  --purple-dark:#26063a;
  --red:#b3131d;
  --red-light:#cf2a31;
  --text:#333;
  --muted:#777;
  --line:#dcdcdc;
  --footer:#353535;
  --footer-bar:#2b2b2b;
  --heading-font:"Nunito Sans",sans-serif;
  --body-font:"Open Sans",sans-serif;
}
*{box-sizing:border-box;margin:0;padding:0}
html,body{width:1200px;height:2222px;overflow:hidden;background:#fff}
body{font-family:var(--body-font);color:var(--text)}
h2,h3,h4{font-weight:400}
.page{position:relative;width:1200px;height:2222px;overflow:hidden;border-top:3px solid var(--red)}
.abs{position:absolute}

/* header */
.brand{left:107px;top:24px;display:flex;align-items:center;gap:12px}
.brand-dot{width:64px;height:64px;border-radius:50%;background:var(--purple)}
.brand-name{font-family:var(--heading-font);font-weight:800;font-size:27px;line-height:29px;color:var(--purple);text-transform:uppercase}
.search{left:793px;top:41px;width:308px;height:38px;display:flex;border:1px solid #cfcfcf}
.search-input{flex:1;font-size:14px;color:#888;padding:10px 12px}
.search-btn{width:44px;background:var(--purple);display:flex;align-items:center;justify-content:center}

/* nav */
.nav{left:98px;top:115px;width:1003px;height:48px;display:flex;background:linear-gradient(var(--purple-light),var(--purple-dark))}
.nav-item{flex:1;display:flex;align-items:center;justify-content:center;color:#fff;font-size:13px;text-transform:uppercase;border-left:1px solid rgba(255,255,255,.15)}
.nav-item:first-child{border-left:0;background:linear-gradient(var(--red-light),#9a0e17);flex:0 0 124px}

/* slider */
.hero{left:98px;top:172px;width:1003px;height:476px;background:linear-gradient(180deg,#2f5f9c 0%,#6d9ccd 38%,#aac4de 52%,#3c6f2a 70%,#2f7a1f 100%)}
.hero-arrow{top:188px}
.hero-title{left:487px;top:155px;font-family:var(--heading-font);font-weight:800;font-size:33px;color:#fff}
.hero-text{left:487px;top:199px;width:420px;font-size:14.5px;line-height:20px;color:#fff}
.hero-btn{left:487px;top:243px;width:119px;height:38px;background:var(--purple);color:#fff;font-size:13px;display:flex;align-items:center;justify-content:center}
.hero-bar{left:0;top:426px;width:1003px;height:50px;background:rgba(25,25,25,.92);display:flex;align-items:center;justify-content:space-between;padding:0 8px 0 20px}
.hero-bar-text{color:#fff;font-size:17px}
.hero-bar-btn{background:var(--red);color:#fff;font-size:13px;padding:9px 10px}

/* panels */
.panel{border:1px solid var(--line);background:#fff}
.panel-title{font-family:var(--heading-font);font-size:22px;font-weight:400;color:var(--purple);text-transform:uppercase}
.panel-title span{color:var(--red)}
.photo{background:linear-gradient(135deg,#2c6a2a,#5b9b3b 55%,#c9d8e4)}
.photo.night{background:linear-gradient(135deg,#121820,#2c3b48 55%,#3f7a2e)}
.photo.red{background:linear-gradient(135deg,#6a9f3e,#b3322f 50%,#3a7a2a)}

.story{left:20px;width:633px;height:176px}
.story .photo{position:absolute;left:0;top:0;width:279px;height:176px}
.story-body{position:absolute;left:297px;top:4px;width:336px}
.story-title{font-family:var(--heading-font);font-size:19px;font-weight:400;color:#222;margin-bottom:8px}
.meta{font-size:11.5px;color:#666;display:flex;align-items:center;gap:5px;margin-bottom:6px}
.cal{display:inline-block;width:10px;height:10px;border:1.5px solid #777;border-top-width:3px}
.com{display:inline-block;width:11px;height:9px;border:1.3px solid #777;border-radius:50%;margin-left:6px}
.story-text{font-size:12.5px;line-height:23px;color:#333}
.btn-more{display:inline-flex;align-items:center;justify-content:center;width:86px;height:33px;background:var(--purple);color:#fff;font-size:12px;margin-top:12px}

.lead-photo{left:20px;top:52px;width:307px;height:218px}
.lead-title{left:20px;top:298px;width:300px;font-size:14px;line-height:21px;font-weight:400;color:var(--red)}
.lead-meta{left:20px;top:344px}
.lead-text{left:20px;top:362px;width:310px;font-size:12.5px;line-height:21px}
.mini{left:355px;width:300px;height:83px}
.mini .photo{position:absolute;left:0;top:0;width:91px;height:83px}
.mini-body{position:absolute;left:98px;top:0;width:205px}
.mini-title{font-size:13.5px;font-weight:700;color:#222;margin-bottom:5px}
.mini-text{font-size:12px;line-height:20px}

/* pagination */
.pager{left:98px;top:1850px;width:671px;height:33px}
.page-btn{position:absolute;top:0;height:33px;width:36px;display:flex;align-items:center;justify-content:center;font-size:12px;color:#444;background:linear-gradient(#f4f4f4,#d9d9d9);border:1px solid #bbb;border-radius:3px}
.page-btn.active{background:var(--red);color:#fff;border-color:#8c0d15}
.page-btn.wide{width:93px;font-size:11px;color:var(--purple)}

/* sidebar */
.side-head{height:49px;background:linear-gradient(var(--purple-light),var(--purple-dark));color:#fff;font-family:var(--heading-font);font-size:21px;text-transform:uppercase;display:flex;align-items:center;justify-content:space-between;padding:0 12px;white-space:nowrap}
.league-head{position:absolute;left:0;top:72px;width:100%;text-align:center}
.league-head b{display:block;font-size:13.5px;line-height:18px;color:#222}
.league-head small{display:block;font-size:12px;line-height:16px;color:#555}
.league-ball{width:44px;height:44px;border-radius:50%;border:3px solid var(--purple);margin:8px auto 0}
.fixtures{position:absolute;left:12px;top:173px;width:287px}
.fixture{display:flex;align-items:center;height:43px;border-top:1px solid var(--line);font-size:12px;color:#333}
.flag{width:22px;height:14px;margin:0 12px 0 18px}
.fixture .home{width:86px}
.fixture .time{width:40px}
.event{left:12px;width:290px;height:86px}
.event .photo{position:absolute;left:0;top:0;width:90px;height:86px}
.event-body{position:absolute;left:99px;top:0;width:195px}
.advert{left:788px;top:1581px;width:313px;height:300px}
.advert .photo{position:absolute;left:0;top:49px;width:313px;height:251px;background:linear-gradient(135deg,#1a1c22,#5a2a2a 45%,#2a4a22)}
.play{left:139px;top:100px}

/* footer */
.footer{left:0;top:1921px;width:1200px;height:246px;background:var(--footer);color:#ddd}
.foot-title{position:absolute;top:28px;font-family:var(--heading-font);font-size:21px;font-weight:400;color:#eee}
.foot-list{position:absolute;top:63px;list-style:none;font-size:12.5px;line-height:24px;color:#eee}
.foot-list li::before{content:"›";margin-right:8px}
.post{position:absolute;left:313px;width:250px;height:76px}
.post .photo{position:absolute;left:0;top:0;width:83px;height:75px}
.post-body{position:absolute;left:98px;top:0;font-size:12.5px;line-height:18px}
.post-title{color:#ccc}
.post-date{font-size:11px;font-style:italic;color:#ccc}
.news-text{position:absolute;left:849px;top:67px;width:260px;font-size:12.5px;line-height:19px;color:#ddd}
.news-input{position:absolute;left:846px;top:110px;width:253px;height:39px;background:#fff;color:#666;font-size:12px;padding:11px 10px}
.news-btn{position:absolute;left:847px;top:159px;width:123px;height:39px;background:var(--red);color:#fff;font-size:13px;display:flex;align-items:center;justify-content:center}
.foot-bar{left:0;top:2167px;width:1200px;height:55px;background:var(--footer-bar);color:#ccc;font-size:12px}
.copyright{left:99px;top:20px}
.social{top:11px;width:33px;height:33px;border-radius:50%}
</style>
</head>
<body>
<div class="page">

  <header>
    <div class="abs brand">
      <div class="brand-dot"></div>
      <div class="brand-name">Corvan<br>Sports</div>
    </div>
    <div class="abs search">
      <div class="search-input">Enter your keywords...</div>
      <div class="search-btn">
        <svg width="18" height="18" viewBox="0 0 18 18"><circle cx="7.5" cy="7.5" r="5.5" fill="none" stroke="#fff" stroke-width="2.4"/><line x1="11.5" y1="11.5" x2="16" y2="16" stroke="#fff" stroke-width="2.6" stroke-linecap="round"/></svg>
      </div>
    </div>
    <nav class="abs nav">
      <div class="nav-item">Home</div>
      <div class="nav-item">About us</div>
      <div class="nav-item">Events</div>
      <div class="nav-item">News</div>
      <div class="nav-item">Gallery</div>
      <div class="nav-item">Testimony</div>
      <div class="nav-item">Contact</div>
    </nav>
  </header>

  <section class="abs hero" role="img" aria-label="Footballer striking a ball in a stadium under a blue sky">
    <svg class="abs hero-arrow" style="left:26px" width="18" height="56" viewBox="0 0 18 56"><polyline points="16,2 2,28 16,54" fill="none" stroke="#fff" stroke-width="1.5"/></svg>
    <svg class="abs hero-arrow" style="left:960px" width="18" height="56" viewBox="0 0 18 56"><polyline points="2,2 16,28 2,54" fill="none" stroke="#fff" stroke-width="1.5"/></svg>
    <div class="abs hero-title">CORVAN SPORTS</div>
    <p class="abs hero-text">Football news from different leagues across Europe and the rest of the World.football news from different leagues</p>
    <div class="abs hero-btn">View more</div>
    <div class="abs hero-bar">
      <span class="hero-bar-text">Different leagues across Europe and the rest of the World...</span>
      <span class="hero-bar-btn">Watch Varnolite</span>
    </div>
  </section>

  <section class="abs panel" style="left:98px;top:683px;width:671px;height:664px">
    <h2 class="abs panel-title" style="left:18px;top:16px">Sports <span>News</span></h2>
    <article class="abs story" style="top:62px">
      <div class="photo night" role="img" aria-label="Player in blue kit sliding for the ball under floodlights"></div>
      <div class="story-body">
        <h3 class="story-title">The standard Lorem Ipsum</h3>
        <div class="meta"><i class="cal"></i>Nov 03 , 2015 <i class="com"></i>4 comments</div>
        <p class="story-text">Lorem Ipsum is simply dummy text of the printing and typesetting industry. Lorem Ipsum has been the industry's standard dummy text.Lorem Ipsum is simply dummy text of the printing and typesetting industry.</p>
        <span class="btn-more">View more</span>
      </div>
    </article>
    <article class="abs story" style="top:259px">
      <div class="photo red" role="img" aria-label="Players in red and yellow kits contesting the ball"></div>
      <div class="story-body">
        <h3 class="story-title">Sed ut perspiciatis unde omnis</h3>
        <div class="meta"><i class="cal"></i>Nov 03 , 2015 <i class="com"></i>4 comments</div>
        <p class="story-text">Lorem Ipsum is simply dummy text of the printing and typesetting industry. Lorem Ipsum has been the industry's standard dummy text.Lorem Ipsum is simply dummy text of the printing and typesetting industry.</p>
        <span class="btn-more">View more</span>
      </div>
    </article>
    <article class="abs story" style="top:458px">
      <div class="photo" role="img" aria-label="Players in green and white kits chasing the ball"></div>
      <div class="story-body">
        <h3 class="story-title">Tempora natus error sit voluptatem</h3>
        <div class="meta"><i class="cal"></i>Nov 03 , 2015 <i class="com"></i>4 comments</div>
        <p class="story-text">Lorem Ipsum is simply dummy text of the printing and typesetting industry. Lorem Ipsum has been the industry's standard dummy text.Lorem Ipsum is simply dummy text of the printing and typesetting industry.</p>
        <span class="btn-more">View more</span>
      </div>
    </article>
  </section>

  <section class="abs panel" style="left:98px;top:1375px;width:671px;height:452px">
    <h2 class="abs panel-title" style="left:18px;top:18px">Football <span>News</span></h2>
    <div class="abs photo lead-photo" role="img" aria-label="Players in blue and white kits competing on the pitch"></div>
    <h3 class="abs lead-title">Sed ut perspiciatis unde omnis iste natus error sit voluptatem</h3>
    <div class="abs meta lead-meta">224 <i class="com"></i>01 Comments</div>
    <p class="abs lead-text">Lorem Ipsum is simply dummy text of the printing and typesetting industry. Lorem Ipsum has been the industry's standard dummy text</p>

    <article class="abs mini" style="top:53px">
      <div class="photo" role="img" aria-label="Goalkeeper diving on grass"></div>
      <div class="mini-body"><h4 class="mini-title">The standard Lorem Ipsum</h4><div class="meta"><i class="cal"></i>Nov 03 , 2015 <i class="com"></i>4 comments</div><p class="mini-text">Lorem Ipsum is simply dummy text of the printing and typesetting</p></div>
    </article>
    <article class="abs mini" style="top:151px">
      <div class="photo night" role="img" aria-label="Player dribbling at night"></div>
      <div class="mini-body"><h4 class="mini-title">The standard Lorem Ipsum</h4><div class="meta"><i class="cal"></i>Nov 03 , 2015 <i class="com"></i>4 comments</div><p class="mini-text">Lorem Ipsum is simply dummy text of the printing and typesetting</p></div>
    </article>
    <article class="abs mini" style="top:250px">
      <div class="photo night" role="img" aria-label="Two players challenging for the ball"></div>
      <div class="mini-body"><h4 class="mini-title">The standard Lorem Ipsum</h4><div class="meta"><i class="cal"></i>Nov 03 , 2015 <i class="com"></i>4 comments</div><p class="mini-text">Lorem Ipsum is simply dummy text of the printing and typesetting</p></div>
    </article>
    <article class="abs mini" style="top:348px">
      <div class="photo red" role="img" aria-label="Player in red kit running with the ball"></div>
      <div class="mini-body"><h4 class="mini-title">The standard Lorem Ipsum</h4><div class="meta"><i class="cal"></i>Nov 03 , 2015 <i class="com"></i>4 comments</div><p class="mini-text">Lorem Ipsum is simply dummy text of the printing and typesetting</p></div>
    </article>
  </section>

  <nav class="abs pager">
    <span class="page-btn wide" style="left:0">&lt;&lt; PREV</span>
    <span class="page-btn active" style="left:102px">1</span>
    <span class="page-btn" style="left:145px">2</span>
    <span class="page-btn" style="left:189px">3</span>
    <span class="page-btn" style="left:232px">4</span>
    <span class="page-btn" style="left:276px">5</span>
    <span class="page-btn" style="left:319px">6</span>
    <span class="page-btn" style="left:363px">7</span>
    <span class="page-btn" style="left:406px">8</span>
    <span class="page-btn" style="left:450px">9</span>
    <span class="page-btn" style="left:493px">10</span>
    <span class="page-btn" style="left:537px">11</span>
    <span class="page-btn wide" style="left:576px">NEXT &gt;&gt;</span>
  </nav>

  <aside class="abs panel" style="left:788px;top:683px;width:313px;height:350px">
    <div class="side-head">Different Leagues</div>
    <div class="league-head"><b>ACROSS EUROPE</b><small>Qualifying Round 1</small><div class="league-ball"></div></div>
    <div class="fixtures">
      <div class="fixture"><span class="flag" style="background:#2a3f9a"></span><span class="home">Arvel FC</span><span class="time">17:00</span><span>FC Serrano</span></div>
      <div class="fixture"><span class="flag" style="background:#d9d9e6"></span><span class="home">B36 Norvik</span><span class="time">19:00</span><span>Vellano FC</span></div>
      <div class="fixture"><span class="flag" style="background:#e0b21c"></span><span class="home">Tre Colline</span><span class="time">20:30</span><span>New Harbour FC</span></div>
      <div class="fixture"><span class="flag" style="background:#2b3f8c"></span><span class="home">Tre Colline</span><span class="time">20:30</span><span>New Harbour FC</span></div>
    </div>
  </aside>

  <aside class="abs panel" style="left:788px;top:1055px;width:313px;height:501px">
    <div class="side-head">Latest Events <svg width="22" height="14" viewBox="0 0 22 14"><polyline points="7,1 1,7 7,13" fill="none" stroke="#fff" stroke-width="1.8"/><polyline points="15,1 21,7 15,13" fill="none" stroke="#fff" stroke-width="1.8"/></svg></div>
    <article class="abs event" style="top:69px">
      <div class="photo" role="img" aria-label="Player kicking a ball on grass"></div>
      <div class="event-body"><h4 class="mini-title">The standard Lorem Ipsum</h4><div class="meta"><i class="cal"></i>Nov 03 , 2015 <i class="com"></i>4 comments</div><p class="mini-text">Lorem Ipsum is simply dummy text of the printing and type</p></div>
    </article>
    <article class="abs event" style="top:173px">
      <div class="photo" role="img" aria-label="Match action in a stadium"></div>
      <div class="event-body"><h4 class="mini-title">The standard Lorem Ipsum</h4><div class="meta"><i class="cal"></i>Nov 03 , 2015 <i class="com"></i>4 comments</div><p class="mini-text">Lorem Ipsum is simply dummy text of the printing and type</p></div>
    </article>
    <article class="abs event" style="top:276px">
      <div class="photo red" role="img" aria-label="Players contesting a header"></div>
      <div class="event-body"><h4 class="mini-title">The standard Lorem Ipsum</h4><div class="meta"><i class="cal"></i>Nov 03 , 2015 <i class="com"></i>4 comments</div><p class="mini-text">Lorem Ipsum is simply dummy text of the printing and type</p></div>
    </article>
    <article class="abs event" style="top:380px">
      <div class="photo night" role="img" aria-label="Player volleying the ball at night"></div>
      <div class="event-body"><h4 class="mini-title">The standard Lorem Ipsum</h4><div class="meta"><i class="cal"></i>Nov 03 , 2015 <i class="com"></i>4 comments</div><p class="mini-text">Lorem Ipsum is simply dummy text of the printing and type</p></div>
    </article>
  </aside>

  <aside class="abs advert">
    <div class="side-head">Special Match Advert <svg width="22" height="14" viewBox="0 0 22 14"><polyline points="7,1 1,7 7,13" fill="none" stroke="#fff" stroke-width="1.8"/><polyline points="15,1 21,7 15,13" fill="none" stroke="#fff" stroke-width="1.8"/></svg></div>
    <div class="photo" role="img" aria-label="Video still of players battling in front of goal">
      <svg class="abs play" width="36" height="36" viewBox="0 0 36 36"><circle cx="18" cy="18" r="18" fill="rgba(0,0,0,.55)"/><polygon points="14,10 26,18 14,26" fill="#fff"/></svg>
    </div>
  </aside>

  <footer class="abs footer">
    <h3 class="foot-title" style="left:95px">Menu</h3>
    <ul class="foot-list" style="left:99px"><li>Home</li><li>About Us</li><li>Events</li><li>News</li><li>Gallery</li><li>Testimony</li><li>Contact</li></ul>

    <h3 class="foot-title" style="left:311px">Recent posts</h3>
    <div class="post" style="top:63px">
      <div class="photo red" role="img" aria-label="Player running with the ball"></div>
      <div class="post-body"><div class="post-title">Finibus Bonorum et</div><div class="post-date">January 24, 2015</div><div>Lorem Ipsum is simply<br>dummy text</div></div>
    </div>
    <div class="post" style="top:150px">
      <div class="photo red" role="img" aria-label="Player dribbling past a defender"></div>
      <div class="post-body"><div class="post-title">Treasury Yields Reach</div><div class="post-date">January 24, 2015</div><div>Lorem Ipsum is simply<br>dummy text</div></div>
    </div>

    <h3 class="foot-title" style="left:630px">Support</h3>
    <ul class="foot-list" style="left:632px"><li>Privacy Policy</li><li>Terms &amp; Conditions</li><li>Sitemap</li></ul>

    <h3 class="foot-title" style="left:846px">News letter</h3>
    <p class="news-text">Sed ut perspiciatis unde omnis iste natus error sit voluptatem accusantium</p>
    <div class="news-input">Enter your email address.....</div>
    <div class="news-btn">Submit</div>
  </footer>

  <div class="abs foot-bar">
    <span class="abs copyright">Copyright 2016 &nbsp;Corvan Sports. All Rights Reserved</span>
    <span class="abs social" style="left:992px;background:#3b5a9a"></span>
    <span class="abs social" style="left:1030px;background:#2ea7e0"></span>
    <span class="abs social" style="left:1068px;background:#c4302b"></span>
  </div>

</div>
</body>
</html>
```